Taboun Dinner, Dessert and Drinks Menu

We need to redesign our Dinner, Desserts, and Drinks Menus.
I have attached all three menus as pdfs. I have chosen the higher payment option because its a few pages and have removed the refund option
Taboun is the most popular Lebanese Restaurant in Melbourne and is a combination of Great Quality Traditional Food and a clean warm ambiance.
Updates
The main part of the menu is the Banquets Section. We want to push our Banquets.
The main focus of the drinks is Lebanese Wines, Lebanese Beer, Lebanese Drinks. Anything Traditional
For the Coffee Menu,
We will be Adding a Chai Latte, More Flavoured Loose Leaf Teas and Removing the Stick Tea. We will also be adding 4 coffee flavour shots to our menu.
Industry/Entity Type
Restaurant
Look and feel
Each slider illustrates characteristics of the customer's brand and the style your logo design should communicate.

```html
<!DOCTYPE html>
<html lang="en">
<head>
<meta charset="utf-8">
<title>Taboun Banquets</title>
<link href="https://fonts.googleapis.com/css2?family=Oswald:wght@600;700&family=Abril+Fatface&family=Open+Sans:ital,wght@0,400;0,600;0,700;1,400;1,700&display=swap" rel="stylesheet">
<style>
  :root{
    --green:#6f8f1e;
    --green-dark:#4f6b12;
    --orange:#e07a12;
    --ink:#2a2320;
    --body:#4a4440;
    --paper:#ffffff;
    --food-1:#e9c98a;
    --food-2:#c9572b;
  }
  *{margin:0;padding:0;box-sizing:border-box}
  html,body{width:849px;height:1200px;overflow:hidden;background:var(--paper)}
  .menu{position:relative;width:849px;height:1200px;font-family:"Open Sans",Arial,sans-serif;color:var(--body)}
  .title{position:absolute;left:28px;top:26px;font-family:"Oswald",Impact,sans-serif;font-weight:700;font-size:62px;line-height:1;color:var(--green);letter-spacing:2px}
  .tagline{position:absolute;left:30px;top:102px;font-size:21px;font-style:italic;color:var(--green);letter-spacing:1px}
  .intro{position:absolute;left:30px;top:142px;width:620px;font-size:14.5px;line-height:1.45;color:var(--body)}
  .brand{position:absolute;right:16px;top:18px;width:170px;height:100px;background:var(--green-dark);display:flex;align-items:center;justify-content:center;border-radius:4px}
  .brand span{font-family:"Oswald",Impact,sans-serif;font-weight:700;font-size:36px;color:#fff;letter-spacing:2px}
  .food{position:absolute;left:640px;top:400px;width:209px;height:680px;border-radius:110px 0 0 110px;background:radial-gradient(circle at 50% 22%,var(--food-2) 0,#d98a4a 25%,transparent 45%),radial-gradient(circle at 55% 72%,var(--food-1) 0,#f1e2b8 30%,transparent 55%),linear-gradient(180deg,#b5c56a 0%,#e6d3a3 45%,#f3ead2 100%)}
  .banquet{position:absolute;left:30px;width:420px}
  .banquet h2{font-family:"Abril Fatface",Georgia,serif;font-weight:400;font-size:35px;line-height:1.1;color:var(--ink);margin-bottom:8px}
  .banquet p{font-size:12.5px;font-style:italic;line-height:1.4;color:var(--body)}
  .price{position:absolute;left:468px;width:165px;font-size:13px;line-height:1.5;color:var(--green)}
  .price .group{display:block;font-size:10.5px;font-weight:700;color:var(--ink);margin:4px 0 0}
  .price .alt{color:var(--orange)}
  .notes{position:absolute;left:0;width:849px;top:1090px;text-align:center}
  .notes .veg{font-size:14px;font-weight:700;color:var(--ink);line-height:1.35}
  .notes .card{margin-top:12px;font-size:15px;font-weight:700;font-style:italic;color:var(--orange);line-height:1.35}
</style>
</head>
<body>
<main class="menu">
  <h1 class="title">TABOUN BANQUETS</h1>
  <p class="tagline">A TRADITIONAL LEBANESE EXPERIENCE</p>
  <p class="intro">A banquet is a terrific way to share and sample an extensive range of the most popular Lebanese dishes. We serve a wide selection of mouth watering entrées and main courses followed by dessert and your choice of Lebanese coffee or Lebanese Loose Leaf tea. Only $2.00 extra if you prefer other coffees or teas from our menu. (min. 2 people per table)</p>

  <div class="brand"><span>TABOUN</span></div>

  <div class="food" role="img" aria-label="Photograph of Lebanese dishes: hummus, tabouleh, olives, dips and fresh herbs"></div>

  <section class="banquet" style="top:285px">
    <h2>Taboun Banquet</h2>
    <p>7 mouthwatering entrées plus a main course of a skewer each of our delicious Shish Kafta and Shish Tawook served with house salad and rice.</p>
  </section>
  <div class="price" style="top:300px">$36.95 per person<span class="group">Groups of 8 or More</span><span class="alt">$34.95 per person</span></div>

  <section class="banquet" style="top:420px">
    <h2>Cedar Banquet</h2>
    <p>10 delicious dips and entrées to start with followed by a wonderful selection of mains. Our chefs change the entrées and mains monthly and include entrées that are especially made for the banquets.</p>
  </section>
  <div class="price" style="top:435px">$47.95 per person<span class="group">Groups of 8 or More</span><span class="alt">$44.95 per person</span></div>

  <section class="banquet" style="top:560px">
    <h2>Banquet with Seafood</h2>
    <p>Similar to the Cedar Banquet but served with Calamari, and spicy prawns plus samke harra as the main and one skewer of lamb or chicken.</p>
  </section>
  <div class="price" style="top:560px">$52.95 per person<span class="group">Groups of 8 or More</span><span class="alt">$49.95 per person</span></div>

  <section class="banquet" style="top:690px">
    <h2>Royal Banquet</h2>
    <p>A feast fit for a king! 16 table filling dips and entrées to start with followed by a wonderful selection of mains that will make everyone feel like royalty!</p>
  </section>
  <div class="price" style="top:700px">$62.95 per person<span class="group">Groups of 8 or More</span><span class="alt">$59.95 per person</span></div>

  <section class="banquet" style="top:830px">
    <h2>Seafood Royal Banquet</h2>
    <p>Similar to the Royal Banquet but served with Calamari, Taboun Prawns and Spicy Prawns plus Samke Harra as the main with a selection of other mains.</p>
  </section>
  <div class="price" style="top:840px">$69.95 per person<span class="group">Groups of 8 or More</span><span class="alt">$64.95 per person</span></div>

  <section class="banquet" style="top:960px">
    <h2>Childrens Banquet</h2>
    <p>Dip, salad, sambousik, and chicken wings followed by a choice of fish fingers and chips or nuggets and chips. Yummy ice cream for dessert.</p>
  </section>
  <div class="price" style="top:975px">$19.95 per person<br><span class="alt">(up to 12 years old)</span></div>

  <footer class="notes">
    <p class="veg">VEGETARIAN OPTIONS AVAILABLE FOR ALL BANQUETS<br>WE CAN ALSO ACCOMMODATE MOST DIETARY REQUIREMENTS</p>
    <p class="card">Please note, a 2% credit card surcharge will apply to all credit card transactions<br>(including where you select the ‘credit’ option when paying by debit card).</p>
  </footer>
</main>
</body>
</html>
```